Keelstone Advisory - Careerloom Header

I am a solopreneur with a consulting company. I do management consulting for small and mid-size manufacturers. There are two ways my prospects check me out - my web page, which went live this week (www.keelstoneadvisory.example), and my personal Careerloom page. I'm working on my Careerloom page now, and I'd like to have a header image that is unique and aligned with my brand.

My clients are smaller manufacturers, typically with 50-400 people. They are privately held, often by an individual or family, but sometimes by a professional investment group. They aren't as sophisticated as the Corvane 300 guys, and sometimes they struggle to grow because their processes break, or they don't have the right people or something else like that. I help them get through those issues.

Many of the people visiting the site will have a technical/engineering orientation, and most are in their late 40's to early 60's.

From my research, I think the image for my personal page is 1584x396, and this will be my primary page. The business page has a banner image size of 1536x768. I'd like to be able to use the same image in both.

Target Market(s)

Small and Mid-size manufacturers - C-Suite executives

Industry/Entity Type

Manufacturing

Font styles to use
Sans Serif

Colors

Designer to choose colors to be used in the design.

Requirements
Must have
• Logo incorporated. Be adaptable to both my personal Careerloom page and Business page, which have slightly different sizes.

```html
<!DOCTYPE html>
<html lang="en">
<head>
<meta charset="utf-8">
<title>Keelstone Advisory – Careerloom Header</title>
<link href="https://fonts.googleapis.com/css2?family=Bebas+Neue&family=Roboto:wght@500&display=swap" rel="stylesheet">
<style>
  :root {
    --page-bg: #e9eaec;
    --navy: #232a63;
    --navy-deep: #151a3c;
    --orange: #f2a416;
    --white: #ffffff;
    --ink: #1d1f2a;
    --photo-a: #2b3160;
    --photo-b: #4a4f78;
    --photo-c: #1b1f3f;
  }
  * { margin: 0; padding: 0; box-sizing: border-box; }
  html, body { width: 1200px; height: 1200px; overflow: hidden; background: var(--page-bg); }
  .canvas { position: relative; width: 1200px; height: 1200px; }

  .banner { position: absolute; left: 89px; width: 1022px; overflow: hidden; }
  .banner--profile { top: 168px; height: 508px; }
  .banner--business { top: 778px; height: 254px; }

  .banner__photo {
    position: absolute; inset: 0;
    background:
      radial-gradient(ellipse at 30% 60%, rgba(120,125,170,.45), transparent 55%),
      radial-gradient(ellipse at 80% 25%, rgba(140,145,185,.35), transparent 50%),
      linear-gradient(135deg, var(--photo-b), var(--photo-a) 45%, var(--photo-c));
  }
  .banner__shapes { position: absolute; inset: 0; width: 100%; height: 100%; }

  .brand { position: absolute; display: flex; align-items: center; gap: 10px; }
  .brand__dot { border-radius: 50%; background: var(--navy); flex: none; }
  .brand__name {
    font-family: "Bebas Neue", sans-serif; color: var(--navy);
    line-height: .95; letter-spacing: .5px;
  }

  .headline, .subline {
    position: absolute; left: 0; right: 0; text-align: center;
    font-family: "Bebas Neue", sans-serif; color: var(--white);
  }

  .contact__phone {
    position: absolute; display: flex; align-items: center; justify-content: center; gap: 8px;
    background: var(--navy); color: var(--white); border-radius: 20px;
    font-family: "Roboto", sans-serif; font-weight: 500;
  }
  .contact__web {
    position: absolute; text-align: center; color: var(--ink);
    font-family: "Roboto", sans-serif; font-weight: 500;
  }

  /* profile sizes */
  .banner--profile .brand { left: 72px; top: 26px; }
  .banner--profile .brand__dot { width: 40px; height: 40px; }
  .banner--profile .brand__name { font-size: 27px; }
  .banner--profile .headline { top: 184px; font-size: 52px; }
  .banner--profile .subline { top: 255px; font-size: 24px; line-height: 33px; }
  .banner--profile .contact__phone { left: 694px; top: 438px; width: 250px; height: 28px; font-size: 13px; }
  .banner--profile .contact__web { left: 680px; width: 272px; top: 472px; font-size: 16px; }

  /* business sizes */
  .banner--business .brand { left: 36px; top: 13px; }
  .banner--business .brand__dot { width: 28px; height: 28px; }
  .banner--business .brand__name { font-size: 19px; }
  .banner--business .headline { top: 70px; font-size: 42px; }
  .banner--business .subline { top: 126px; font-size: 19px; line-height: 28px; }
  .banner--business .contact__phone { left: 793px; top: 209px; width: 193px; height: 22px; font-size: 11px; }
  .banner--business .contact__web { left: 780px; width: 220px; top: 236px; font-size: 12.5px; }
</style>
</head>
<body>
<main class="canvas">

  <section class="banner banner--profile" aria-label="Profile header">
    <div class="banner__photo" role="img" aria-label="Photo of business partners shaking hands over a desk with reports and a laptop, tinted navy"></div>
    <svg class="banner__shapes" viewBox="0 0 1022 508" aria-hidden="true">
      <path d="M0,0 H440 C480,20 470,80 420,108 C370,134 270,140 170,132 C90,126 30,112 0,100 Z" fill="var(--orange)"/>
      <path d="M0,0 H420 C460,20 455,75 405,100 C355,124 265,130 170,122 C90,116 30,104 0,92 Z" fill="var(--navy)"/>
      <path d="M0,0 H405 C440,20 435,68 390,90 C345,110 260,116 170,110 C90,104 30,94 0,82 Z" fill="var(--white)"/>
      <line x1="121" y1="24" x2="121" y2="78" stroke="var(--navy)" stroke-width="1.5"/>
      <path d="M580,508 C585,420 680,372 850,372 C940,372 1000,382 1022,390 V508 Z" fill="var(--orange)"/>
      <path d="M592,508 C598,430 690,384 850,384 C940,384 1000,394 1022,402 V508 Z" fill="var(--navy)"/>
      <path d="M606,508 C612,440 700,396 855,398 C945,400 1000,410 1022,418 V508 Z" fill="var(--white)"/>
    </svg>
    <div class="brand">
      <span class="brand__dot"></span>
      <span class="brand__name">Keelstone<br>Advisory</span>
    </div>
    <h1 class="headline">Enabling Manufacturers to Break Through</h1>
    <p class="subline">Keelstone Advisory specializes in helping small- and mid-sized manufacturers to break through to<br>new levels of growth, scalability and financial performance</p>
    <div class="contact__phone">
      <svg width="15" height="15" viewBox="0 0 24 24" aria-hidden="true"><circle cx="12" cy="12" r="11" fill="none" stroke="var(--white)" stroke-width="2"/><path d="M8.5 6.5l2 2-1.2 1.6c.8 1.7 2 2.9 3.6 3.6l1.6-1.2 2 2-1.3 1.8c-3.9-.5-7.6-4.2-8.1-8.1z" fill="var(--white)"/></svg>
      <span>555-014-2370</span>
    </div>
    <div class="contact__web">www.keelstoneadvisory.example</div>
  </section>

  <section class="banner banner--business" aria-label="Business page banner">
    <div class="banner__photo" role="img" aria-label="Photo of business partners shaking hands over a desk with reports, tinted navy"></div>
    <svg class="banner__shapes" viewBox="0 0 1022 254" aria-hidden="true">
      <path d="M0,0 H232 C255,12 250,52 215,70 C180,84 120,88 70,84 C40,81 15,76 0,70 Z" fill="var(--orange)"/>
      <path d="M0,0 H220 C242,12 238,48 205,64 C172,78 118,82 70,78 C40,75 15,70 0,64 Z" fill="var(--navy)"/>
      <path d="M0,0 H210 C230,12 226,44 196,58 C166,71 115,75 70,72 C40,69 15,64 0,58 Z" fill="var(--white)"/>
      <line x1="74" y1="13" x2="74" y2="44" stroke="var(--navy)" stroke-width="1.2"/>
      <path d="M735,254 C740,200 800,166 900,164 C960,163 1000,168 1022,174 V254 Z" fill="var(--orange)"/>
      <path d="M745,254 C750,206 808,174 900,172 C960,171 1000,176 1022,182 V254 Z" fill="var(--navy)"/>
      <path d="M756,254 C762,214 816,182 902,181 C960,181 1000,186 1022,190 V254 Z" fill="var(--white)"/>
    </svg>
    <div class="brand">
      <span class="brand__dot"></span>
      <span class="brand__name">Keelstone<br>Advisory</span>
    </div>
    <h2 class="headline">Enabling Manufacturers to Break Through</h2>
    <p class="subline">Keelstone Advisory specializes in helping small- and mid-sized manufacturers to break through to<br>new levels of growth, scalability and financial performance</p>
    <div class="contact__phone">
      <svg width="12" height="12" viewBox="0 0 24 24" aria-hidden="true"><circle cx="12" cy="12" r="11" fill="none" stroke="var(--white)" stroke-width="2"/><path d="M8.5 6.5l2 2-1.2 1.6c.8 1.7 2 2.9 3.6 3.6l1.6-1.2 2 2-1.3 1.8c-3.9-.5-7.6-4.2-8.1-8.1z" fill="var(--white)"/></svg>
      <span>555-014-2370</span>
    </div>
    <div class="contact__web">www.keelstoneadvisory.example</div>
  </section>

</main>
</body>
</html>
```